law firm business cards

I need a business card using my existing logo. Two sided is best because there is a lot of information that needs to go on the card. Use the same general color scheme as logo, but I need one set with the blue background of my website (www.kestonlegalgroup.com), and one set with white background (to see which one I like best).

Information that must be on there:
Darren P. Holloway
Board Certified Civil Trial Specialist
738 Brindlewood Ave., Suite 2300
Raleigh, NC 27699

T 919-555-0142
F 919-555-0187

www.kestonlegalgroup.com
darren@kestonlegalgroup.com

Personal Injury | Criminal Law (to separate the two, pls use a bullet point or pipeline symbol "|"

If there is a way to work in the QRVC logo (maybe at the bottom somewhere), put it in, but don't let it detract from the main logo too much.

Also, if there is a way to work it in, put in somewhere: Former Insurance Company Attorney | Former Criminal Prosecutor (to separate the two, pls use a bullet point or pipeline symbol "|"

```html
<!DOCTYPE html>
<html lang="en">
<head>
<meta charset="utf-8">
<title>Keston Legal Group – Business Cards</title>
<link rel="stylesheet" href="https://fonts.googleapis.com/css2?family=Noto+Serif:wght@400;500&display=swap">
<style>
  :root {
    --stage: #2c2c2c;
    --navy: #1f3a69;
    --navy-ink: #1f2d5c;
    --silver: #e6e7ec;
    --tagline: #d9dbe3;
    --paper: #ffffff;
    --ink: #141414;
    --font-text: "Noto Serif", Georgia, serif;
  }
  * { box-sizing: border-box; margin: 0; padding: 0; }
  html, body { width: 1200px; height: 1000px; overflow: hidden; }
  body { background: var(--stage); font-family: var(--font-text); position: relative; }

  .card { position: absolute; left: 260px; width: 681px; height: 388px; }
  .card--front { top: 87px; background: var(--navy); }
  .card--back { top: 525px; background: var(--paper); color: var(--ink); }

  .firm-name { position: absolute; white-space: nowrap; font-weight: 400; text-transform: uppercase; letter-spacing: 1px; }
  .card--front .firm-name { left: 70px; top: 150px; font-size: 42px; color: var(--silver); }
  .card--back .firm-name { left: 27px; top: 38px; font-size: 27px; color: var(--navy-ink); }

  .practice-areas {
    position: absolute; right: 79px; top: 243px;
    font-size: 16.5px; letter-spacing: 1.6px; color: var(--tagline); text-transform: uppercase;
  }

  .cert-seal { position: absolute; left: 573px; top: 24px; width: 82px; height: 82px; }

  .attorney { position: absolute; left: 0; right: 0; top: 157px; text-align: center; }
  .attorney__name { font-size: 31px; font-weight: 400; letter-spacing: 1.5px; text-transform: uppercase; line-height: 1.1; }
  .attorney__title { font-size: 17.5px; letter-spacing: 0.6px; margin-top: 4px; }

  .contact { position: absolute; list-style: none; font-size: 18.5px; letter-spacing: 0.8px; line-height: 25.5px; }
  .contact--phones { left: 27px; top: 269px; }
  .contact--web { left: 336px; top: 267px; }
  .contact li { display: flex; align-items: flex-start; }
  .contact svg { width: 14px; height: 14px; margin-top: 6px; margin-right: 11px; flex: none; fill: var(--ink); }
  .contact .indent { padding-left: 25px; }
</style>
</head>
<body>

<section class="card card--front" aria-label="Front of card">
  <h1 class="firm-name">Keston Legal Group</h1>
  <p class="practice-areas">Personal Injury | Criminal Law</p>
</section>

<section class="card card--back" aria-label="Back of card">
  <p class="firm-name">Keston Legal Group</p>

  <svg class="cert-seal" viewBox="0 0 82 82" role="img" aria-label="Board certification seal">
    <circle cx="41" cy="41" r="39" fill="none" stroke="#1f2d5c" stroke-width="2"/>
    <circle cx="41" cy="41" r="26" fill="none" stroke="#1f2d5c" stroke-width="2"/>
  </svg>

  <div class="attorney">
    <h2 class="attorney__name">Darren P. Holloway</h2>
    <p class="attorney__title">Board Certified Civil Trial Specialist</p>
  </div>

  <ul class="contact contact--phones">
    <li>
      <svg viewBox="0 0 16 16" aria-hidden="true"><path d="M1 5c0-2 3-3 7-3s7 1 7 3v1h-4V4.5H5V6H1zM3 7h10l2 6H1z"/></svg>
      919.555.0142
    </li>
    <li>
      <svg viewBox="0 0 16 16" aria-hidden="true"><path d="M4 1h8v14H4zM5.5 2.5v9h5v-9zM7 12.5h2v1.2H7z" fill-rule="evenodd"/></svg>
      919.555.0163
    </li>
    <li>
      <svg viewBox="0 0 16 16" aria-hidden="true"><path d="M4 1h7l1 1v3H4zM1 6h14v7h-3v2H4v-2H1zM5 10v4h6v-4z" fill-rule="evenodd"/></svg>
      919.555.0187
    </li>
  </ul>

  <ul class="contact contact--web">
    <li>
      <svg viewBox="0 0 16 16" aria-hidden="true"><path d="M1 3h14v10H1zM2.5 4.5l5.5 4.5 5.5-4.5v7h-11z" fill-rule="evenodd"/></svg>
      darren@kestonlegalgroup.com
    </li>
    <li>
      <svg viewBox="0 0 16 16" aria-hidden="true"><circle cx="8" cy="8" r="7"/><path d="M5 4c2 0 2 2 4 2s1 3-1 3-2 3-3 3-1-3-2-4 0-4 2-4zM11 10c1 0 2 1 1 2s-2 0-1-2z" fill="#fff"/></svg>
      www.kestonlegalgroup.com
    </li>
    <li>
      <svg viewBox="0 0 16 16" aria-hidden="true"><path d="M8 1a5 5 0 0 1 5 5c0 4-5 9-5 9S3 10 3 6a5 5 0 0 1 5-5zm0 3a2 2 0 1 0 0 4 2 2 0 0 0 0-4z" fill-rule="evenodd"/></svg>
      738 Brindlewood Ave., Suite 2300
    </li>
    <li class="indent">Raleigh, NC 27699</li>
  </ul>
</section>

</body>
</html>
```